Training Company Needs a Web Design

We are a Training company that needs a website design completed for us. "The Harbor Loft" The website will be a 'community space' specialising in 'Change and Transformation'. It will be a 'space' where individuals can come to find out 'latest news', upcoming events and courses, chat with others and find 'tools and templates'. They will need to login as a 'Member'.

The final design needs to be professional but have a 'fun and interactive' feel and appeal to our target audience who are predominantly corporate individuals.

Target Market(s)

Corporate Individuals - they may have a Change or Project background

Industry/Entity Type

Business Consultant

Number of Pages Required

3 page

Font styles to use
Sans Serif

Requirements
Must have
• Design for 'Home Page'
• A professional and corporate 'feel' but be fun and interactive.
Nice to have
• A 'sense' of how some of the other pages may be designed or laid out.

```html
<!DOCTYPE html>
<html lang="en">
<head>
<meta charset="utf-8">
<title>The Harbor Loft — Home</title>
<link href="https://fonts.googleapis.com/css2?family=Montserrat:ital,wght@0,400;0,500;0,600;0,700;1,400;1,600&family=Open+Sans:ital,wght@0,400;0,600;0,700;1,400&display=swap" rel="stylesheet">
<style>
:root{
  --navy:#0b4d8a;
  --cyan:#10a3db;
  --ink:#333;
  --muted:#666;
  --line:#ccc;
  --white:#fff;
  --dark:#111;
  --tile:#4a4a4a;
}
*{box-sizing:border-box;margin:0;padding:0}
html,body{width:670px;height:1200px;overflow:hidden;background:var(--white)}
body{position:relative;font-family:"Open Sans",sans-serif;color:var(--ink)}
h1,h2,h3{font-weight:400}
.abs{position:absolute}

/* header */
.site-header{left:0;top:0;width:670px;height:38px;background:var(--white)}
.brand{left:152px;top:14px;display:flex;align-items:center;gap:5px;font-family:"Montserrat",sans-serif;font-weight:600;font-size:7px;color:var(--navy);line-height:9px;text-transform:uppercase;white-space:nowrap}
.brand .mark{width:9px;height:9px;border:2px solid var(--cyan)}
.nav-link{top:17px;font-family:"Montserrat",sans-serif;font-size:5.2px;color:#444;text-transform:uppercase;white-space:nowrap;line-height:7px}
.nav-link.current{color:var(--cyan);font-weight:600}
.login-btn{left:482px;top:13px;width:37px;height:15px;background:var(--cyan);color:var(--white);font-family:"Montserrat",sans-serif;font-size:5.2px;font-weight:600;text-align:center;line-height:15px;text-transform:uppercase}

/* hero */
.hero-photo{left:0;top:38px;width:670px;height:193px;background:linear-gradient(120deg,#5a3f34 0%,#7b6a5f 30%,#9a8f86 55%,#6d5d52 80%,#3f3029 100%)}
.hero-shade{left:0;top:38px;width:670px;height:193px;background:rgba(0,0,0,.35)}
.hero-title{left:0;width:670px;top:108px;text-align:center;color:var(--white);font-family:"Montserrat",sans-serif;font-weight:600;font-size:12px;letter-spacing:.3px}
.hero-sub{left:195px;width:280px;top:126px;text-align:center;color:var(--white);font-family:"Montserrat",sans-serif;font-size:4.9px;line-height:8.5px;text-transform:uppercase}
.hero-btn{left:304px;top:160px;width:62px;height:16px;background:var(--cyan);color:var(--white);font-family:"Montserrat",sans-serif;font-size:5.2px;font-weight:600;text-align:center;line-height:16px;text-transform:uppercase}
.dots{display:flex;gap:2px}
.dots i{width:5px;height:5px;border-radius:50%;border:1px solid var(--white);display:block}
.dots i.on{background:var(--cyan);border-color:var(--cyan)}

/* services */
.section-title{left:0;width:670px;text-align:center;top:256px;color:var(--navy);font-family:"Montserrat",sans-serif;font-size:8.5px;font-weight:500}
.section-intro{left:215px;width:240px;top:271px;text-align:center;font-size:4.8px;line-height:8px;color:var(--muted)}
.service{top:304px;width:144px;height:159px;text-align:center}
.service.active{background:var(--navy);color:var(--white)}
.service .ring{position:absolute;left:46px;top:14px;width:52px;height:52px;border-radius:50%;border:1px solid #bbb;display:flex;align-items:center;justify-content:center}
.service.active .ring{border-color:var(--white)}
.service h3{position:absolute;left:0;width:144px;top:78px;font-family:"Montserrat",sans-serif;font-size:5.8px;color:#555}
.service.active h3{color:var(--white)}
.service .rule{position:absolute;left:55px;width:34px;top:92px;height:1px;background:var(--line)}
.service.active .rule{background:rgba(255,255,255,.5)}
.service p{position:absolute;left:22px;width:100px;top:101px;font-size:4.6px;line-height:8px;color:var(--muted)}
.service.active p{color:var(--white)}
.service .more{position:absolute;left:50px;top:131px;width:44px;height:14px;border:1px solid #bbb;font-family:"Montserrat",sans-serif;font-size:4.2px;line-height:12px;color:var(--muted);background:var(--white)}
.service.active .more{color:var(--navy);border-color:var(--white)}
.divider{left:150px;width:368px;top:490px;height:1px;background:#e6e6e6}

/* events & news */
.block-title{left:150px;font-family:"Montserrat",sans-serif;font-size:7.8px;color:#333;text-transform:uppercase;white-space:nowrap}
.short-rule{left:150px;width:17px;height:1px;background:var(--line)}
.block-text{left:150px;width:130px;font-size:4.6px;line-height:8px;color:var(--muted)}
.view-all{left:150px;font-size:4px;color:#777;text-transform:uppercase}
.event-photo{top:518px;height:64px}
.event-date{font-size:4.4px;font-style:italic;color:#777}
.card-title{font-size:4.8px;font-weight:700;color:#444;line-height:8px}
.mini-rule{width:17px;height:1px;background:var(--line)}
.read-more{font-size:4px;color:#555;text-transform:uppercase}
.read-more.hot{color:var(--navy)}

.quote-band{left:0;top:650px;width:670px;height:131px;background:linear-gradient(90deg,#3a3a3a 0%,#222 40%,#1a1a1a 70%,#0e0e0e 100%)}
.quote-mark{left:325px;top:677px;width:20px;height:20px;border-radius:50%;border:1px solid var(--cyan);color:var(--white);font-family:"Montserrat",sans-serif;font-weight:700;font-size:11px;text-align:center;line-height:22px}
.quote-text{left:192px;width:286px;top:706px;text-align:center;color:var(--white);font-family:"Montserrat",sans-serif;font-size:5.4px;line-height:10px}
.quote-author{left:0;width:670px;top:734px;text-align:center;color:var(--white);font-family:"Montserrat",sans-serif;font-size:5.8px;font-style:italic}
.quote-author b{color:var(--cyan);font-style:normal}

.date-tile{width:22px;height:21px;background:var(--tile);color:var(--white);text-align:center;font-family:"Montserrat",sans-serif}
.date-tile.hot{background:var(--navy)}
.date-tile b{display:block;font-size:9px;line-height:12px;font-weight:600}
.date-tile small{display:block;font-size:4.5px;line-height:6px}

/* footer */
.site-footer{left:0;top:971px;width:670px;height:197px;background:var(--navy)}
.footer-title{top:996px;color:var(--white);font-family:"Montserrat",sans-serif;font-size:7.8px;text-transform:uppercase}
.footer-text{left:150px;top:1015px;width:180px;color:var(--white);font-size:4.6px;line-height:8px}
.contact-row{left:150px;display:flex;align-items:center;gap:9px;color:#cfe0f0;font-size:5.4px;line-height:8px}
.contact-row .icon{width:13px;height:13px;border-radius:50%;background:rgba(255,255,255,.12);display:flex;align-items:center;justify-content:center}
.field{left:350px;width:168px;border:1px solid rgba(255,255,255,.35);color:#9fbfdc;font-size:5.2px;padding:5px 8px}
.send-btn{left:350px;top:1130px;width:168px;height:20px;background:var(--white);color:var(--navy);font-family:"Montserrat",sans-serif;font-size:5.6px;font-weight:500;text-align:center;line-height:20px;text-transform:uppercase}
.bottom-bar{left:0;top:1168px;width:670px;height:32px;background:var(--dark)}
.bottom-brand{left:152px;top:1176px;width:38px;color:var(--white);font-family:"Montserrat",sans-serif;font-weight:600;font-size:5.4px;line-height:7px;text-transform:uppercase}
.bottom-sep{left:194px;top:1176px;width:1px;height:17px;background:#555}
.copyright{left:206px;top:1182px;color:#aaa;font-size:4.4px;white-space:nowrap}
.social{top:1178px;display:flex;gap:3px;left:464px}
.social i{display:block;width:12px;height:12px;border-radius:50%;border:1px solid #ddd}
</style>
</head>
<body>

<header class="abs site-header">
  <div class="abs brand"><span class="mark"></span>The Harbor Loft</div>
  <nav>
    <span class="abs nav-link current" style="left:304px">Home</span>
    <span class="abs nav-link" style="left:336px">About Us</span>
    <span class="abs nav-link" style="left:378px">News</span>
    <span class="abs nav-link" style="left:412px">Blog</span>
    <span class="abs nav-link" style="left:445px">Contact Us</span>
  </nav>
  <div class="abs login-btn">Login</div>
</header>

<section>
  <div class="abs hero-photo" role="img" aria-label="Photo of a team gathered around a table working together with notes and laptops"></div>
  <div class="abs hero-shade"></div>
  <h1 class="abs hero-title">CHANGE AND TRANSFORMATION</h1>
  <p class="abs hero-sub">Phasellus porta. Fusce susct varius mi. Cum sociis natoque penabus et magnis dis parturient montes, nascetur ridiculus mus. Nulla dui. Fusce feugiat malesuada odio.</p>
  <div class="abs hero-btn">Learn More</div>
  <svg class="abs" style="left:89px;top:142px" width="10" height="14" viewBox="0 0 10 14"><path d="M8 1 2 7l6 6" fill="none" stroke="#fff" stroke-width="1.3"/></svg>
  <svg class="abs" style="left:571px;top:142px" width="10" height="14" viewBox="0 0 10 14"><path d="M2 1l6 6-6 6" fill="none" stroke="#fff" stroke-width="1.3"/></svg>
  <div class="abs dots" style="left:324px;top:208px"><i></i><i class="on"></i><i></i><i></i></div>
</section>

<section>
  <h2 class="abs section-title">WE MEET YOUR COMMUNITY SPACE</h2>
  <p class="abs section-intro">Sed ut perspiciatis unde omnis iste natus error sit voluptatem accusantium doloremque laudantium,totam rem aperiam, eaque ipsa quae ab illo inventore veritatis et quasi architecto beatae vitae dicta.</p>

  <div class="abs service" style="left:132px">
    <div class="ring"><svg width="20" height="18" viewBox="0 0 20 18"><rect x="1" y="1" width="18" height="12" rx="1" fill="#555"/><rect x="7" y="14" width="6" height="2" fill="#555"/><rect x="5" y="16" width="10" height="1.5" fill="#555"/></svg></div>
    <h3>TOOLS AND TEMPLATES</h3><div class="rule"></div>
    <p>Nemo enim ipsam voluptatem quia voluptas sit aspernatur aut odit aut fugit, sed quia consequuntur</p>
    <div class="more">LEARN MORE</div>
  </div>
  <div class="abs service active" style="left:273px">
    <div class="ring"><svg width="20" height="18" viewBox="0 0 20 18"><path d="M1 2h11v8H5l-3 3v-3H1z" fill="#fff"/><path d="M13 5h6v8h-1v3l-3-3H8v-2h5z" fill="#fff"/></svg></div>
    <h3>COMMUNITY SPACE</h3><div class="rule"></div>
    <p>Nemo enim ipsam voluptatem quia voluptas sit aspernatur aut odit aut fugit, sed quia consequuntur</p>
    <div class="more">LEARN MORE</div>
  </div>
  <div class="abs service" style="left:389px">
    <div class="ring"><svg width="20" height="20" viewBox="0 0 20 20" stroke="#555" stroke-width="1.2" fill="#555"><line x1="10" y1="10" x2="3" y2="3"/><line x1="10" y1="10" x2="17" y2="3"/><line x1="10" y1="10" x2="3" y2="17"/><line x1="10" y1="10" x2="17" y2="17"/><circle cx="10" cy="10" r="2.6"/><circle cx="3" cy="3" r="1.8"/><circle cx="17" cy="3" r="1.8"/><circle cx="3" cy="17" r="1.8"/><circle cx="17" cy="17" r="1.8"/></svg></div>
    <h3>SPECIALISATION</h3><div class="rule"></div>
    <p>Nemo enim ipsam voluptatem quia voluptas sit aspernatur aut odit aut fugit, sed quia consequuntur</p>
    <div class="more">LEARN MORE</div>
  </div>
  <div class="abs divider"></div>
</section>

<section>
  <h2 class="abs block-title" style="top:517px">Upcoming Events &amp; Courses</h2>
  <div class="abs short-rule" style="top:536px"></div>
  <p class="abs block-text" style="top:543px">Lorem ipsum dolor sit amet, consectetur adipiscing elit, sed do eiusmod tempor incididunt ut labore et dolore magna aliqua. Ut enim ad minim veniam, quis nostrud exercitation ullamco laboris nisi</p>
  <div class="abs view-all" style="top:588px">View All</div>

  <div class="abs event-photo" style="left:300px;width:104px;background:linear-gradient(135deg,#c9b27a 0%,#6a8d8f 45%,#2f5560 100%)" role="img" aria-label="Photo of a woman working at a café table"></div>
  <div class="abs event-photo" style="left:414px;width:104px;background:linear-gradient(135deg,#b79a86 0%,#8c7162 50%,#5b4a42 100%)" role="img" aria-label="Photo of a bicycle parked by a city wall"></div>
  <div class="abs event-date" style="left:300px;top:588px">28 Feb 2016</div>
  <div class="abs card-title" style="left:300px;top:597px">Duis aute irure dolor in reprehenderit</div>
  <div class="abs mini-rule" style="left:300px;top:610px"></div>
  <div class="abs read-more hot" style="left:300px;top:615px">Read More</div>
  <div class="abs event-date" style="left:414px;top:588px">28 Feb 2016</div>
  <div class="abs card-title" style="left:414px;top:597px">Duis aute irure dolor in reprehenderit</div>
  <div class="abs mini-rule" style="left:414px;top:609px"></div>
  <div class="abs read-more" style="left:414px;top:613px">Read More</div>
</section>

<section>
  <div class="abs quote-band" role="img" aria-label="Dark photo of business people shaking hands"></div>
  <div class="abs quote-mark">“</div>
  <p class="abs quote-text">Lorem ipsum dolor sit amet, consectetur adipisicing elit, sed do eiusmod incididunt ut labore et dolore magna aliqua. Ut enim ad minim veniam...</p>
  <p class="abs quote-author"><b>Sam Rivera</b> - USA, Detroit</p>
  <div class="abs dots" style="left:324px;top:755px"><i class="on"></i><i></i><i></i></div>
</section>

<section>
  <h2 class="abs block-title" style="top:809px">Latest News</h2>
  <div class="abs short-rule" style="top:828px"></div>
  <p class="abs block-text" style="top:835px">Lorem ipsum dolor sit amet, consectetur adipiscing elit, sed do eiusmod tempor incididunt ut labore et dolore magna aliqua.</p>
  <div class="abs view-all" style="top:873px">View All</div>

  <div class="abs date-tile hot" style="left:300px;top:810px"><b>28</b><small>FEB</small></div>
  <div class="abs card-title" style="left:300px;top:837px;width:110px">Duis aute irure dolor in reprehenderit in voluptate velit esse cillum dolore</div>
  <div class="abs mini-rule" style="left:300px;top:858px"></div>
  <div class="abs read-more hot" style="left:300px;top:863px">Read More</div>

  <div class="abs date-tile" style="left:421px;top:810px"><b>28</b><small>FEB</small></div>
  <div class="abs card-title" style="left:421px;top:837px;width:110px">Duis aute irure dolor in reprehenderit in voluptate velit esse cillum dolore</div>
  <div class="abs mini-rule" style="left:421px;top:858px"></div>
  <div class="abs read-more" style="left:421px;top:863px">Read More</div>

  <div class="abs date-tile" style="left:300px;top:887px"><b>28</b><small>FEB</small></div>
  <div class="abs card-title" style="left:300px;top:914px;width:110px">Duis aute irure dolor in reprehenderit in voluptate velit esse cillum dolore</div>
  <div class="abs mini-rule" style="left:300px;top:935px"></div>
  <div class="abs read-more" style="left:300px;top:940px">Read More</div>

  <div class="abs date-tile" style="left:421px;top:887px"><b>28</b><small>FEB</small></div>
  <div class="abs card-title" style="left:421px;top:914px;width:110px">Duis aute irure dolor in reprehenderit in voluptate velit esse cillum dolore</div>
  <div class="abs mini-rule" style="left:421px;top:935px"></div>
  <div class="abs read-more" style="left:421px;top:940px">Read More</div>
</section>

<footer>
  <div class="abs site-footer"></div>
  <h2 class="abs footer-title" style="left:150px">Contact Us</h2>
  <p class="abs footer-text">Duis aute irure dolor in reprehenderit in voluptate velit esse cillum dolore eu fugiat nulla pariatur. Excepteur sint occaecat cupidatat non proident</p>
  <div class="abs contact-row" style="top:1044px">
    <span class="icon"><svg width="6" height="8" viewBox="0 0 6 8"><path d="M3 0a3 3 0 0 0-3 3c0 2 3 5 3 5s3-3 3-5a3 3 0 0 0-3-3zm0 4a1 1 0 1 1 0-2 1 1 0 0 1 0 2z" fill="#9fbfdc"/></svg></span>
    <span>123, Street Name, City Name<br>Country Name 12345</span>
  </div>
  <div class="abs contact-row" style="top:1064px;font-size:7px">
    <span class="icon"><svg width="7" height="7" viewBox="0 0 7 7"><path d="M1 0l1.5 1.8-.8 1a4 4 0 0 0 1.6 1.6l1-.8L7 5.1 6 7C3 7 0 4 0 1z" fill="#9fbfdc"/></svg></span>
    <span>(+123) 1234 - 1234</span>
  </div>
  <div class="abs contact-row" style="top:1085px;color:#fff">
    <span class="icon"><svg width="7" height="5" viewBox="0 0 7 5"><rect width="7" height="5" fill="#9fbfdc"/><path d="M0 0l3.5 2.6L7 0" fill="none" stroke="#0b4d8a" stroke-width=".7"/></svg></span>
    <span>info@example.com</span>
  </div>

  <h2 class="abs footer-title" style="left:351px">Leave a Message</h2>
  <div class="abs field" style="top:1014px;height:19px">Your Name*</div>
  <div class="abs field" style="top:1035px;height:19px">Your Email Address*</div>
  <div class="abs field" style="top:1056px;height:19px">Phone Number</div>
  <div class="abs field" style="top:1078px;height:48px">Message*</div>
  <div class="abs send-btn">Send Message</div>

  <div class="abs bottom-bar"></div>
  <div class="abs bottom-brand">The Harbor<br>Loft</div>
  <div class="abs bottom-sep"></div>
  <div class="abs copyright">© All Right Reserved 2016. Company Name</div>
  <div class="abs social"><i></i><i></i><i></i><i></i></div>
</footer>

</body>
</html>
```